brochure for payroll services

we need a brochure design for our new payroll services- either to be send to prospect as an email attachment or print. see attached on content required.
our corporate colour is orange . the design should communicate trust ,and reliability with a breadth of fresh air.

```html
<!DOCTYPE html>
<html lang="en">
<head>
<meta charset="utf-8">
<title>Tresvale Payroll Services Brochure</title>
<link href="https://fonts.googleapis.com/css2?family=Cabin:wght@400;500;600&display=swap" rel="stylesheet">
<style>
  :root {
    --orange: #f7941d;
    --ink: #231f20;
    --paper: #ffffff;
    --backdrop: #e9e9eb;
    --band-text: #ffffff;
  }
  * { margin: 0; padding: 0; box-sizing: border-box; }
  html, body {
    width: 1040px; height: 1200px; overflow: hidden;
    background: var(--backdrop);
    font-family: "Cabin", "Gill Sans", sans-serif;
    color: var(--ink);
  }
  .brochure {
    position: absolute; left: 222px; top: 191px;
    width: 606px; height: 861px;
    background: var(--paper);
    box-shadow: 0 10px 30px rgba(0,0,0,0.12);
  }
  .section-title {
    position: absolute; left: 32px;
    font-size: 30px; font-weight: 500; line-height: 1;
    display: flex; align-items: flex-end;
  }
  .section-title::after {
    content: ""; display: block; height: 3px; background: var(--orange);
    margin-left: 9px; margin-bottom: 6px;
  }
  .title-advantages { top: 43px; }
  .title-advantages::after { width: 297px; }
  .title-scope { top: 290px; }
  .title-scope::after { width: 316px; }
  .title-related { top: 533px; }
  .title-related::after { width: 257px; }

  .list { position: absolute; left: 32px; list-style: none; }
  .list li { position: relative; padding-left: 19px; }
  .list li::before {
    content: ">"; position: absolute; left: 0; top: 0; color: var(--orange);
  }
  .advantages { top: 82px; width: 540px; font-size: 17.5px; line-height: 22px; }
  .advantages li { margin-bottom: 11px; }
  .advantages li:nth-child(2), .advantages li:nth-child(3) { margin-bottom: 10px; }

  .scope-intro {
    position: absolute; left: 32px; top: 318px;
    font-size: 17px; color: var(--orange);
  }
  .scope { top: 346px; font-size: 13px; line-height: 20.4px; }
  .related { top: 567px; font-size: 13px; line-height: 20.4px; }
  .related li { color: var(--orange); }
  .related li::before { color: var(--ink); }

  .brand {
    position: absolute; right: 36px; top: 596px;
    display: flex; align-items: center; gap: 7px;
    font-size: 19px; font-weight: 500;
  }
  .brand-square { width: 16px; height: 16px; background: var(--orange); }

  .contact-band {
    position: absolute; left: 0; top: 673px; width: 606px; height: 188px;
    background: var(--orange); color: var(--band-text);
  }
  .band-notch { position: absolute; left: 33px; top: 0; }
  .band-heading {
    position: absolute; left: 48px; top: 50px;
    font-size: 20px; font-weight: 500; letter-spacing: 0.2px; text-transform: uppercase;
  }
  .address {
    position: absolute; left: 48px; top: 91px;
    font-style: normal; font-size: 15px; line-height: 20.5px;
  }
  .band-divider {
    position: absolute; left: 335px; top: 98px; width: 1px; height: 53px;
    background: rgba(255,255,255,0.8);
  }
  .web-contact { position: absolute; left: 354px; top: 91px; }
  .email { font-size: 15px; line-height: 20px; display: block; }
  .website { font-size: 21px; line-height: 22px; font-weight: 500; display: block; }
</style>
</head>
<body>
  <main class="brochure">
    <h2 class="section-title title-advantages">Our advantages</h2>
    <ul class="list advantages">
      <li>Project management and methodology to ensure seamless transition and sustainable delivery</li>
      <li>Domain knowledge in payroll, accounting &amp; finance and tax</li>
      <li>Robust technology platform for automation, control and visibility</li>
      <li>Proven delivery expertise and experience to provide reliable and trusted services</li>
    </ul>

    <h2 class="section-title title-scope">Scope of services</h2>
    <p class="scope-intro">The scope of services include the following :</p>
    <ul class="list scope">
      <li>Process payroll (salary calculation) on monthly to bi-monthly (ie. twice a month) basis</li>
      <li>Process gross to net salary and applicable CPF, CDAC, MBMF, SINDA or ECF contribution</li>
      <li>Process bonuses, and any adhoc payments</li>
      <li>Process no pay leave</li>
      <li>Salary disbursement to employees via Bank GIRO transfer</li>
      <li>Provide payroll report for management's review</li>
      <li>Prepare and submit CPF e-submission</li>
      <li>Prepare and submit year-end tax forms (Form IR8A)</li>
    </ul>

    <h2 class="section-title title-related">Other related services</h2>
    <ul class="list related">
      <li>Employee's leave administration and management</li>
      <li>Timesheet management</li>
      <li>Claim management</li>
    </ul>

    <div class="brand"><span class="brand-square"></span><span>Tresvale</span></div>

    <footer class="contact-band">
      <svg class="band-notch" width="38" height="34" viewBox="0 0 38 34" aria-hidden="true">
        <polygon points="0,0 38,0 19,34" fill="#ffffff"/>
      </svg>
      <h3 class="band-heading">Contact us to explore how we can help you</h3>
      <address class="address">
        Tresvale Private Limited<br>
        45 Kallor Road, #02-11, Harbour Point<br>
        Singapore 318822
      </address>
      <div class="band-divider"></div>
      <div class="web-contact">
        <span class="email">hello@tresvale.biz</span>
        <span class="website">www.tresvale.biz</span>
      </div>
    </footer>
  </main>
</body>
</html>
```